SloPitch Ad

Looking for a creative eye-catching ad to go on the front page of my website to promote a softball league. Ad dimensions needs to be 1194 by 624, or in that ratio so that it can also be used on facebook.
I have attached some graphics that I have seen on other sites that I like for general ideas. Will need the colors to match with my website (www.pkvathletics.com) but logo is not necessary

```html
<!DOCTYPE html>
<html lang="en">
<head>
<meta charset="utf-8">
<title>Softball Leagues Now Open</title>
<link rel="stylesheet" href="https://fonts.googleapis.com/css2?family=Rubik+Dirt&family=Graduate&family=Black+Ops+One&family=Marcellus&display=swap">
<style>
  :root {
    --dirt-light: #b07a52;
    --dirt-mid: #8c5a38;
    --dirt-dark: #4e2f1b;
    --glove-tone: #a4552c;
    --ball-tone: #d6e83a;
    --headline-white: #ffffff;
    --silver-top: #ffffff;
    --silver-mid: #a9adb3;
    --silver-low: #5d6166;
    --chance-green: #1d4a1a;
    --button-top: #5fae3e;
    --button-bottom: #1f6a14;
    --button-edge: #175010;
    --button-text: #ffffff;
  }
  * { margin: 0; padding: 0; box-sizing: border-box; }
  html, body { width: 1200px; height: 627px; overflow: hidden; background: #ffffff; }
  .ad {
    position: relative;
    width: 1200px;
    height: 627px;
    overflow: hidden;
  }
  .ad__photo {
    position: absolute;
    inset: 0;
    background:
      radial-gradient(circle at 830px 290px, var(--ball-tone) 0, rgba(214,232,58,0.55) 150px, rgba(214,232,58,0) 200px),
      radial-gradient(ellipse 360px 330px at 850px 260px, var(--glove-tone) 0, rgba(164,85,44,0.75) 70%, rgba(164,85,44,0) 100%),
      radial-gradient(ellipse 900px 500px at 400px 380px, var(--dirt-light) 0, var(--dirt-mid) 55%, var(--dirt-dark) 100%);
  }
  .ad__title {
    position: absolute;
    left: 60px;
    top: 42px;
    font-family: "Rubik Dirt", system-ui, sans-serif;
    font-size: 66px;
    letter-spacing: 2px;
    color: var(--headline-white);
    text-shadow: 2px 3px 4px rgba(0,0,0,0.55);
    white-space: nowrap;
  }
  .ad__status {
    position: absolute;
    left: 182px;
    top: 196px;
    font-family: "Graduate", Georgia, serif;
    font-size: 72px;
    letter-spacing: 4px;
    background: linear-gradient(180deg, var(--silver-top) 0%, var(--silver-mid) 48%, var(--silver-low) 52%, var(--silver-top) 100%);
    -webkit-background-clip: text;
    background-clip: text;
    color: transparent;
    filter: drop-shadow(2px 3px 3px rgba(0,0,0,0.6));
    white-space: nowrap;
  }
  .ad__tagline {
    position: absolute;
    left: 62px;
    top: 355px;
    font-family: "Black Ops One", Impact, sans-serif;
    font-size: 62px;
    letter-spacing: 3px;
    color: var(--chance-green);
    text-shadow: 0 0 6px rgba(255,255,255,0.35), 2px 3px 3px rgba(0,0,0,0.5);
    white-space: nowrap;
  }
  .ad__cta {
    position: absolute;
    left: 347px;
    top: 505px;
    width: 510px;
    height: 100px;
    border-radius: 8px;
    border: 2px solid var(--button-edge);
    background: linear-gradient(180deg, var(--button-top) 0%, #3f8f27 45%, var(--button-bottom) 100%);
    box-shadow: 0 3px 6px rgba(0,0,0,0.45), inset 0 1px 0 rgba(255,255,255,0.4);
    display: flex;
    align-items: center;
    justify-content: center;
    font-family: "Marcellus", Georgia, serif;
    font-size: 48px;
    letter-spacing: 1px;
    color: var(--button-text);
    text-shadow: 1px 2px 2px rgba(0,0,0,0.45);
  }
</style>
</head>
<body>
  <main class="ad">
    <div class="ad__photo" role="img" aria-label="Photograph of a yellow softball resting in a brown leather glove on an infield dirt surface"></div>
    <h1 class="ad__title">Softball Leagues</h1>
    <p class="ad__status">NOW OPEN</p>
    <p class="ad__tagline">Don’t miss your Chance!</p>
    <div class="ad__cta">Let’s Play Ball!</div>
  </main>
</body>
</html>
```